Web app for job market trends **

We are building a website where users come to see what skills they will need for their career. The content of the page is data-driven, so the site should have the feel of a set of data dashboards. The data is collected and processed using machine learning. The main idea is for the user to come in and spend some minutes exploring, scrolling and clicking around.
The task is to design a website with four pages:
Front page
Early career page
Skill trends page
Skills Page
Each of these is described in attached files, along with example data
We need the resulting files to be exported also to uncompressed PNG, and in the case of vector graphics, to SVG.
Target Market(s)
People Looking to start a Career and Policy makers.
Industry/Entity Type
Human Resource
Number of Pages Required
4 page
Look and feel

```html
<!DOCTYPE html>
<html lang="en">
<head>
<meta charset="utf-8">
<title>Skillwise – Your personal guide to the skill trends on the job market</title>
<link rel="stylesheet" href="https://fonts.googleapis.com/css2?family=Montserrat:wght@300;400;600;700;800&family=Open+Sans:wght@400;600&display=swap">
<style>
:root{
  --ink:#1b1b1b;
  --text:#2c2c2c;
  --blue:#1f7ad8;
  --link:#2a86e0;
  --grey-bg:#efeeee;
  --panel-bg:#f3f1f1;
  --card-bg:#f4f2f2;
  --footer:#262626;
  --footer-text:#d9d9d9;
  --white:#ffffff;
  --tag:#4a55d9;
}
*{box-sizing:border-box;margin:0;padding:0}
html,body{width:1200px;height:4454px;overflow:hidden}
body{font-family:"Open Sans",Arial,sans-serif;color:var(--text);background:var(--white);position:relative}
.section{position:absolute;left:0;width:1200px}
.abs{position:absolute}
.heading{font-family:"Montserrat",sans-serif;font-weight:800;font-size:24px;color:var(--ink);letter-spacing:.3px}
.heading.underlined::after{content:"";display:block;width:88px;height:3px;background:var(--blue);margin-top:12px}
.heading.centered{text-align:center;width:1200px;left:0}
.heading.centered::after{margin:12px auto 0;width:180px}
.body-copy{font-size:15.5px;line-height:22px;color:var(--text)}
.body-copy p+p{margin-top:22px}
.sub-heading{font-family:"Montserrat",sans-serif;font-weight:700;font-size:17px;color:var(--ink);letter-spacing:.3px}

/* hero */
.hero{top:0;height:676px;background:linear-gradient(160deg,#0f2a3a 0%,#0a1a28 45%,#060d16 100%)}
.brand{font-family:"Montserrat",sans-serif;font-weight:700;color:var(--white)}
.nav-brand{left:29px;top:24px;font-size:28px}
.nav{top:32px;left:0;width:1200px;font-family:"Montserrat",sans-serif;font-weight:700;font-size:14px;color:var(--white)}
.nav span{position:absolute;top:0;white-space:nowrap}
.hero-title{left:631px;top:350px;font-family:"Montserrat",sans-serif;font-weight:800;font-size:40px;color:var(--white);letter-spacing:1px}
.hero-sub{left:631px;top:408px;font-family:"Montserrat",sans-serif;font-weight:300;font-size:32px;line-height:40px;color:var(--white)}

/* motivation */
.motivation{top:676px;height:467px}

/* process */
.process{top:1143px;height:581px;background:var(--grey-bg)}
.search-box{left:133px;top:133px;width:267px;height:55px;background:var(--white);border:1px solid #cfcfcf;font-size:12.5px;color:#333}
.search-box .field{position:absolute;left:18px;top:19px}
.search-box .lang{position:absolute;right:0;top:0;width:56px;height:53px;border-left:1px solid #cfcfcf;padding:18px 0 0 14px}
.trend-chart{left:427px;top:133px;width:342px;height:118px;background:var(--white)}
.job-ad{left:806px;top:133px;width:297px;height:405px;font-size:8.4px;line-height:14.6px;color:#333;padding:2px 4px}
.tag{display:inline-block;border:1px solid var(--tag);color:var(--tag);border-radius:2px;padding:0 4px;line-height:11px;margin:1px 1px}
.feedback{position:absolute;left:2px;top:377px;width:294px;height:26px;display:flex;background:var(--white)}
.feedback div{flex:1;display:flex;align-items:center;justify-content:center}
.feedback .up{border:1px solid #4ab06a}
.feedback .down{border:1px solid #e35a5a}

/* application */
.application{top:1724px;height:916px}

/* about */
.about{top:2640px;height:504px;background:var(--panel-bg)}
.about a{color:var(--link);font-weight:600;text-decoration:none}

/* team */
.team{top:3144px;height:586px}
.card{width:296px;height:398px;background:var(--card-bg);top:136px}
.card .portrait{height:197px}
.card .name{position:absolute;left:24px;top:225px;font-family:"Montserrat",sans-serif;font-weight:700;font-size:14px;color:var(--ink)}
.card .role{position:absolute;left:24px;top:246px;font-size:12px;color:#444}
.card .bio{position:absolute;left:24px;top:276px;width:250px;font-size:12.5px;line-height:18px;color:#333}
.card .profile-btn{position:absolute;left:24px;top:345px;background:var(--blue);color:var(--white);font-family:"Montserrat",sans-serif;font-weight:700;font-size:8.5px;padding:7px 10px;letter-spacing:.3px}

/* support */
.support{top:3730px;height:181px;background:linear-gradient(100deg,#1a6fd0 0%,#2383e0 50%,#1b72d4 100%)}
.support-title{left:131px;top:80px;font-family:"Montserrat",sans-serif;font-weight:800;font-size:29px;color:var(--white);letter-spacing:.5px}
.donate{left:916px;top:69px;width:154px;height:54px;background:var(--white);color:var(--blue);font-family:"Montserrat",sans-serif;font-weight:800;font-size:20px;display:flex;align-items:center;justify-content:center;letter-spacing:.5px}

/* powered by */
.powered{top:3911px;height:201px}

/* footer */
.footer{top:4112px;height:342px;background:var(--footer);color:var(--footer-text)}
.footer-brand{left:134px;top:88px;font-size:44px}
.footer-col-title{font-family:"Montserrat",sans-serif;font-weight:700;font-size:12px;color:var(--white);letter-spacing:.5px}
.footer-menu{font-size:12px;line-height:20px;text-transform:uppercase}
.footer-item{font-size:11.5px;line-height:15px}
.icon-dot{position:absolute;width:24px;height:24px;border-radius:50%;background:var(--white)}
.legal{left:0;width:1200px;top:300px;text-align:center;font-size:11.5px;color:var(--footer-text)}
</style>
</head>
<body>

<!-- Hero -->
<header class="section hero" role="img" aria-label="Dark digital landscape with glowing data streams across a grid">
  <div class="abs brand nav-brand">Skillwise</div>
  <nav class="abs nav">
    <span style="left:697px">HOME</span>
    <span style="left:794px">EARLY CAREER</span>
    <span style="left:960px">SKILL TRENDS</span>
    <span style="left:1113px">SKILLS</span>
  </nav>
  <h1 class="abs hero-title">SKILLWISE</h1>
  <p class="abs hero-sub">Your personal guide to the<br>skill trends on the job market</p>
</header>

<!-- Motivation -->
<section class="section motivation">
  <h2 class="abs heading underlined" style="left:131px;top:62px">MOTIVATION</h2>
  <div class="abs body-copy" style="left:131px;top:132px;width:360px;font-size:15.8px;line-height:25.5px">
    We enable deep and unbiased analysis of the skill demands in the job market. Using deep learning techniques, we achieve understanding of job advertisements to extract the most relevant information for you. We combine these analysis with the most complete structural knowledge repositories to deliver analytics, discover trends and provide recommendations for personal professional development, as well as insightful job market overviews!
  </div>
  <div class="abs" style="left:552px;top:47px;width:517px;height:368px;background:linear-gradient(160deg,#e8f1f8 0%,#c3d8ea 45%,#9fbdd8 100%)" role="img" aria-label="Person standing in front of a large transparent screen showing a world map and business charts"></div>
</section>

<!-- Process -->
<section class="section process">
  <h2 class="abs heading centered" style="top:42px">OUR PROCESS</h2>
  <div class="abs search-box"><span class="field">Enter a skill or a job title</span><span class="lang">EN ▾</span></div>
  <svg class="abs trend-chart" viewBox="0 0 342 118" role="img" aria-label="Line chart of skill demand from 2015 to 2021">
    <g font-family="Courier New, monospace" font-size="5.5" font-weight="700" fill="#222">
      <circle cx="8" cy="5" r="2" fill="#3a5bd9"/><text x="13" y="6">Project</text><text x="13" y="12">Management</text><text x="13" y="18">Skills</text>
      <circle cx="72" cy="10" r="2" fill="#e0315a"/><text x="77" y="12">Pedagogy</text>
      <circle cx="147" cy="5" r="2" fill="#e7b21d"/><text x="152" y="6">Use of</text><text x="152" y="12">Office</text><text x="152" y="18">Software</text>
      <circle cx="205" cy="5" r="2" fill="#2aa760"/><text x="210" y="6">Alternative</text><text x="210" y="12">Teaching</text><text x="210" y="18">Techniques</text>
      <circle cx="285" cy="5" r="2" fill="#8a2fc9"/><text x="290" y="6">Human</text><text x="290" y="12">Resource</text><text x="290" y="18">Management</text>
    </g>
    <g stroke="#eee" stroke-width=".6"><line x1="20" y1="40" x2="335" y2="40"/><line x1="20" y1="60" x2="335" y2="60"/><line x1="20" y1="80" x2="335" y2="80"/><line x1="20" y1="100" x2="335" y2="100"/></g>
    <g fill="none" stroke-width="1.3">
      <polyline stroke="#e0315a" points="20,55 60,60 100,58 140,66 180,62 220,68 260,64 300,70 330,66"/>
      <polyline stroke="#3a5bd9" points="20,48 60,52 100,50 140,56 180,58 220,55 260,60 300,58 330,62"/>
      <polyline stroke="#e7b21d" points="20,75 60,78 100,74 140,80 180,77 220,82 260,80 300,84 330,82"/>
      <polyline stroke="#8a2fc9" points="20,88 60,86 100,90 140,88 180,92 220,90 260,93 300,92 330,94"/>
      <polyline stroke="#2aa760" points="20,98 80,99 140,98 200,99 260,98 300,97 318,90 330,38"/>
    </g>
    <g font-family="Courier New, monospace" font-size="6" font-weight="700" fill="#222">
      <text x="20" y="114">2015</text><text x="70" y="114">2016</text><text x="120" y="114">2017</text><text x="170" y="114">2018</text><text x="220" y="114">2019</text><text x="270" y="114">2020</text><text x="320" y="114">2021</text>
    </g>
  </svg>
  <div class="abs job-ad">
    Your tasks:<br>
    As sales associate you are the first contact for our customers and the friendly, competent point of care <span class="tag">Consulting</span><br>
    and acquisition of new customers<br>
    Handling of requests and shipping of information material<br>
    Preparing offers, tracking and follow-up until the order is placed<br>
    Selling our products by phone<br>
    Acquisition of new customers<br>
    Close cooperation with all departments of the company, intensive<br>
    <span class="tag">Communication</span><span class="tag">Communication</span> with the area <span class="tag">Customer service</span><br>
    <span class="tag">Consulting</span> conversations at trade fairs<br><br>
    What you bring:<br>
    As sales associate you have a completed commercial training<br>
    and ideally two years of sales experience (not required)<br>
    Independence and initiative are natural for you as well as<br>
    confident handling of customer care<br>
    You have good <span class="tag">German</span><span class="tag">German skills</span> in speech and<br>
    writing as well as basic knowledge in <span class="tag">English</span><span class="tag">English</span><br>
    Ambitious sales goals are a challenge you enjoy and you want to help the company grow<br>
    Very good networking and <span class="tag">Communication</span> skills complete your profile
    <div class="feedback">
      <div class="up"><svg width="12" height="12" viewBox="0 0 12 12" aria-label="Helpful"><path d="M1 5h2v6H1zM4 5l3-4c1 0 1.5.6 1.3 1.6L8 4.5h2.5c.8 0 1.2.7 1 1.4l-1.2 4.2c-.2.6-.6.9-1.2.9H4z" fill="none" stroke="#4ab06a" stroke-width=".9"/></svg></div>
      <div class="down"><svg width="12" height="12" viewBox="0 0 12 12" aria-label="Not helpful"><g transform="rotate(180 6 6)"><path d="M1 5h2v6H1zM4 5l3-4c1 0 1.5.6 1.3 1.6L8 4.5h2.5c.8 0 1.2.7 1 1.4l-1.2 4.2c-.2.6-.6.9-1.2.9H4z" fill="none" stroke="#e35a5a" stroke-width=".9"/></g></svg></div>
    </div>
  </div>
</section>

<!-- Application -->
<section class="section application">
  <h2 class="abs heading centered" style="top:60px">OUR APPLICATION</h2>
  <div class="abs" style="left:133px;top:154px;width:441px;height:321px;background:radial-gradient(ellipse at 55% 55%,#c98a4a 0%,#5a3a24 35%,#15161a 75%)" role="img" aria-label="Hands holding a smartphone with glowing data charts rising from the screen"></div>
  <h3 class="abs sub-heading" style="left:624px;top:158px">CHALLENGES</h3>
  <div class="abs body-copy" style="left:624px;top:188px;width:450px;font-size:14.2px;line-height:20px">
    <p>Choosing the correct occupation plays an increasingly important role in our lives. Nowadays we consider an occupation as one of our fundamental rights. Yet, with the complexity of the modern technologies and job markets it is challenging to guarantee equal access to the market for everyone</p>
    <p>The challenges include the knowledge of languages, personal traits, different understanding of requirements and different assessments of personal strengths. On the other end, business owners and recruitment professionals invest lots of effort to find suitable candidates for their job openings. How do we improve the situation, overcome the challenges and enable efficient, unbiased analysis of job advertisements without the need to change the existing practices?”</p>
  </div>
  <h3 class="abs sub-heading" style="left:133px;top:534px">HOW WE DO THIS</h3>
  <div class="abs body-copy" style="left:133px;top:564px;width:452px;font-size:14.2px;line-height:20px">
    We employ machine learning. Machines do not have personal preferences or biases. The impressive progress of natural language processing and deep neural networks power our algorithms to precisely recognize and extract the most important pieces of information. We use manually designed ontologies that set the frames of the analysis and guide the machine in this process. However, machines (and also we ourselves) still miss a lot of background information about our complex professional world -- no one is perfect (yet). To fill in this gap we use the most complete structural knowledge sources to serve as background knowledge and provide additional information about the subject area. The combination of these two methodologies yields human-like processing results at huge scales. This allows us to aggregate data, provide deep insights, and identify novelties in the ever evolving job market.
  </div>
  <div class="abs" style="left:628px;top:529px;width:441px;height:322px;background:radial-gradient(ellipse at 50% 50%,#1e4fb0 0%,#0d2a6a 45%,#050f2a 100%)" role="img" aria-label="Glowing network of connected nodes on a dark blue background"></div>
</section>

<!-- About -->
<section class="section about">
  <div class="abs" style="left:0;top:0;width:576px;height:504px;background:linear-gradient(135deg,#0b1f4a 0%,#1d4fa8 45%,#3c7ad0 70%,#0d2456 100%)" role="img" aria-label="Hand typing on a laptop keyboard surrounded by floating blue binary digits"></div>
  <h2 class="abs heading" style="left:628px;top:56px">ABOUT US</h2>
  <div class="abs body-copy" style="left:628px;top:119px;width:445px;font-size:14.2px;line-height:20px">
    <p>This application is a free social project powered by 3 enthusiast. We are experts in Natural Language Processing and Semantic Web with a record of 50+ scientific publications at top conferences and journals (<a>https://scholar.example.org/citations?user=ab12CDEFgh</a>, <a>https://scholar.example.org/citations?user=xy34KLMNop</a>). We also have training and work experience in HR, and, most importantly passion for the job market. We all have migrant backgrounds and we know how difficult and important it might be to find your place in any new professional environment. Therefore, we strive to provide better professional opportunities, equal access and fair treatment for everyone.</p>
    <p>At the moment the project is completely funded by us. This not only includes the maintenance and further development, but also the costs of the infrastracture. If you like it and want us to continue, please, support us. Your every donation counts.</p>
  </div>
</section>

<!-- Team -->
<section class="section team">
  <h2 class="abs heading centered" style="top:69px">OUR TEAM</h2>
  <article class="abs card" style="left:133px">
    <div class="portrait" style="background:linear-gradient(90deg,#d8d2c8 0%,#8a7a6a 50%,#9a4a36 100%)" role="img" aria-label="Portrait of a team member in a grey blazer in front of a brick wall"></div>
    <div class="name">DANIEL</div><div class="role">Marketing Manager</div>
    <div class="bio">Lorem Ipsum is simply dummy text of the printing and typesetting industry. Lorem Ipsum has been the.</div>
    <div class="profile-btn">VIEW PROFILE</div>
  </article>
  <article class="abs card" style="left:451px">
    <div class="portrait" style="background:linear-gradient(180deg,#c9d6e0 0%,#8fa6b6 55%,#c7b9a6 100%)" role="img" aria-label="Portrait of a team member in a light shirt by the sea"></div>
    <div class="name">MARCO</div><div class="role">Marketing Manager</div>
    <div class="bio">Lorem Ipsum is simply dummy text of the printing and typesetting industry. Lorem Ipsum has been the.</div>
    <div class="profile-btn">VIEW PROFILE</div>
  </article>
  <article class="abs card" style="left:775px">
    <div class="portrait" style="background:radial-gradient(ellipse at 50% 60%,#5a4a44 0%,#2a2426 55%,#141214 100%)" role="img" aria-label="Portrait of a team member in a dark suit against a dark background"></div>
    <div class="name">LUKAS BRENNER</div><div class="role">Marketing Manager</div>
    <div class="bio">Lorem Ipsum is simply dummy text of the printing and typesetting industry. Lorem Ipsum has been the.</div>
    <div class="profile-btn">VIEW PROFILE</div>
  </article>
</section>

<!-- Support -->
<section class="section support">
  <h2 class="abs support-title">SUPPORT US</h2>
  <div class="abs donate">DONATE</div>
</section>

<!-- Powered by -->
<section class="section powered">
  <h2 class="abs heading underlined" style="left:133px;top:66px">POWERED BY</h2>
  <div class="abs" style="left:692px;top:40px;width:152px;height:104px;background:#2c4a9a" role="img" aria-label="Partner badge"></div>
  <div class="abs" style="left:951px;top:40px;width:116px;height:104px;background:#9b1c2e" role="img" aria-label="Partner badge"></div>
</section>

<!-- Footer -->
<footer class="section footer">
  <div class="abs brand footer-brand">Skillwise</div>

  <div class="abs footer-col-title" style="left:439px;top:40px">MENU</div>
  <div class="abs footer-menu" style="left:439px;top:74px">Home<br>Early Career<br>Skill Trends<br>Skills</div>

  <div class="abs footer-col-title" style="left:669px;top:40px">CONTACT US</div>
  <div class="icon-dot" style="left:669px;top:80px"><svg width="24" height="24" viewBox="0 0 24 24" aria-hidden="true"><path d="M12 6a4 4 0 0 0-4 4c0 3 4 8 4 8s4-5 4-8a4 4 0 0 0-4-4zm0 5.5a1.5 1.5 0 1 1 0-3 1.5 1.5 0 0 1 0 3z" fill="#262626"/></svg></div>
  <div class="abs footer-item" style="left:701px;top:78px">2200 Harbor Lane<br>Linden, CA 90000</div>
  <div class="icon-dot" style="left:669px;top:130px"><svg width="24" height="24" viewBox="0 0 24 24" aria-hidden="true"><path d="M8.5 6.5l2 2-1.2 1.6a8 8 0 0 0 4.6 4.6l1.6-1.2 2 2-1.5 1.8c-4.5-.5-8.7-4.7-9.2-9.2z" fill="#262626"/></svg></div>
  <div class="abs footer-item" style="left:701px;top:128px">Call Us<br>555.010.2040</div>
  <div class="icon-dot" style="left:669px;top:180px"><svg width="24" height="24" viewBox="0 0 24 24" aria-hidden="true"><rect x="6.5" y="8" width="11" height="8" rx="1" fill="#262626"/><path d="M6.8 8.5L12 12.5l5.2-4" fill="none" stroke="#fff" stroke-width="1"/></svg></div>
  <div class="abs footer-item" style="left:701px;top:178px">E mail Us<br>info@skillwise.example</div>

  <div class="abs footer-col-title" style="left:963px;top:40px">FOLLOW US</div>
  <div class="icon-dot" style="left:963px;top:80px"></div>
  <div class="abs footer-item" style="left:998px;top:78px">Like us on<br>FRIENDBOOK</div>
  <div class="icon-dot" style="left:963px;top:130px"></div>
  <div class="abs footer-item" style="left:998px;top:128px">Follow us on<br>CHIRPER</div>
  <div class="icon-dot" style="left:963px;top:180px"></div>
  <div class="abs footer-item" style="left:998px;top:178px">Follow us on<br>LINKWORK</div>

  <div class="abs legal">Terms &nbsp; | &nbsp;Privacy | &nbsp;Copyright © 2021 All Rights Reserved</div>
</footer>

</body>
</html>
```